Business Card Design Project

The business card is for an educational company that provides personalised tuition to students.

The company logo is in orange and blue (as provided) and should be included in the name card design

The philosophy of the company is to make learning a comfortable experience for student as such design of the namecard should look fresh and has a bit of the 'wow' factor. Some of the namecard design that appeals to me are as uploaded under Sample Design.

The particulars that need to be provided are:
(1): Company Name (Quillmark Education)
(1): Name
(2): Educational qualifications which will appear below name
(3): Mobile number
(4): Email address
(5): Website

Industry/Entity Type

Business

Requirements
Must have
• (1): Company Logo

(2): The card background should preferably be coloured both for the front side and back.

(3): The choice of font is important as part of the selection consideration. There is no preferred font that I have selected, designer is free to choose the font that will complement their design.

```html
<!DOCTYPE html>
<html lang="en">
<head>
<meta charset="utf-8">
<title>Quillmark Education — Business Card</title>
<link href="https://fonts.googleapis.com/css2?family=Cinzel:wght@500&family=Fira+Sans:wght@400;600&family=Tinos:wght@400;700&display=swap" rel="stylesheet">
<style>
  :root {
    --canvas-bg: #e4e5e7;
    --card-white: #ffffff;
    --ink-dark: #3a3d42;
    --ink-grey: #6f7378;
    --brand-blue: #1f9bd9;
    --brand-blue-deep: #1584c4;
    --brand-orange: #f26a2c;
    --brand-peach: #f9b887;
    --text-light: #ffffff;
  }
  * { box-sizing: border-box; margin: 0; padding: 0; }
  html, body { width: 1200px; height: 960px; overflow: hidden; }
  body {
    background: var(--canvas-bg);
    display: flex;
    flex-direction: column;
    align-items: center;
    justify-content: center;
    gap: 60px;
  }
  .card {
    position: relative;
    width: 700px;
    height: 400px;
    border-radius: 40px;
    overflow: hidden;
    box-shadow: 0 10px 30px rgba(0,0,0,0.18);
  }

  /* Front */
  .card-front { background: var(--card-white); }
  .holder-name {
    position: absolute; left: 70px; top: 62px;
    font-family: "Cinzel", serif; font-weight: 500;
    font-size: 40px; color: var(--ink-dark); letter-spacing: -0.5px;
  }
  .holder-qualifications {
    position: absolute; left: 72px; top: 118px;
    font-family: "Fira Sans", sans-serif;
    font-size: 23px; color: var(--ink-grey);
  }
  .contact-list {
    position: absolute; left: 72px; top: 290px;
    list-style: none;
    font-family: "Fira Sans", sans-serif;
    font-size: 22px; color: var(--ink-grey);
  }
  .contact-list li { display: flex; align-items: center; gap: 12px; height: 34px; }
  .contact-list svg { width: 22px; height: 22px; flex: none; }
  .brand-lockup {
    position: absolute; right: 40px; bottom: 80px;
    display: flex; align-items: center; gap: 14px;
  }
  .brand-square {
    width: 80px; height: 80px; border-radius: 10px;
    background: var(--brand-orange);
  }
  .brand-name {
    font-family: "Tinos", serif; font-weight: 400;
    font-size: 38px; line-height: 1.0; color: var(--ink-dark);
  }

  /* Back */
  .card-back { background: var(--brand-blue); }
  .back-field { position: absolute; inset: 0; width: 100%; height: 100%; }
  .website {
    position: absolute; left: 62px; top: 38px;
    font-family: "Fira Sans", sans-serif; font-weight: 600;
    font-size: 15px; color: var(--text-light); letter-spacing: 0.8px;
  }
  .back-brand-name {
    position: absolute; right: 50px; bottom: 70px;
    font-family: "Tinos", serif; font-weight: 700;
    font-size: 54px; line-height: 0.95; color: var(--text-light);
    text-align: left;
  }
</style>
</head>
<body>

  <section class="card card-front" aria-label="Card front">
    <h1 class="holder-name">YOUR NAME</h1>
    <p class="holder-qualifications">Educational Qualifications</p>
    <ul class="contact-list">
      <li>
        <svg viewBox="0 0 22 22" aria-hidden="true"><rect x="6" y="2" width="10" height="18" rx="2" fill="none" stroke="#6f7378" stroke-width="2"/><rect x="8" y="5" width="6" height="6" fill="#6f7378"/></svg>
        0000 000 000
      </li>
      <li>
        <svg viewBox="0 0 22 22" aria-hidden="true"><rect x="2" y="5" width="18" height="12" fill="none" stroke="#6f7378" stroke-width="2"/><path d="M2 5 L11 12 L20 5" fill="none" stroke="#6f7378" stroke-width="2"/></svg>
        name@quillmark.edu
      </li>
    </ul>
    <div class="brand-lockup">
      <div class="brand-square" aria-hidden="true"></div>
      <div class="brand-name">Quillmark<br>Education</div>
    </div>
  </section>

  <section class="card card-back" aria-label="Card back">
    <svg class="back-field" viewBox="0 0 700 400" preserveAspectRatio="none" aria-hidden="true">
      <defs>
        <linearGradient id="blueField" x1="0" y1="0" x2="1" y2="1">
          <stop offset="0" stop-color="#2aa6e2"/>
          <stop offset="1" stop-color="#1584c4"/>
        </linearGradient>
        <radialGradient id="orangeField" cx="0.8" cy="0.25" r="0.8">
          <stop offset="0" stop-color="#f9c39a"/>
          <stop offset="0.45" stop-color="#f48a4a"/>
          <stop offset="1" stop-color="#ee5f22"/>
        </radialGradient>
      </defs>
      <rect width="700" height="400" fill="url(#blueField)"/>
      <path d="M560 0 C420 60 260 180 200 400 L700 400 L700 0 Z" fill="url(#orangeField)"/>
    </svg>
    <p class="website">www.quillmark.edu</p>
    <div class="back-brand-name">Quillmark<br>Education</div>
  </section>

</body>
</html>
```